"Tales of Quiet Harbors" Book Cover Design

I am seeking a dynamic, modern, and professional cover design for a book focused on groundbreaking science that explores how a supplement called plasmalogens can revitalize the brain, prevent Alzheimer’s, and safeguard memories. The design should strike a balance between being visually appealing and conveying the seriousness of the topic.

Target Market(s)

The target audience includes individuals who are curious about cutting-edge science and proactive approaches to brain health, as well as those seeking to better understand how to protect their cognitive functions and memories. The cover should resonate with readers interested in health, science, and self-improvement, while reflecting the book’s informative and empowering tone.

Requirements
Must have
• The quotation across the top of the page (this is a placeholder for now, it will be changed eventually) and the author's name.
Should not have
• You don't need to use the puzzle idea!

```html
<!DOCTYPE html>
<html lang="en">
<head>
<meta charset="utf-8">
<title>Tales of Quiet Harbors – Book Cover Spread</title>
<link href="https://fonts.googleapis.com/css2?family=Bebas+Neue&family=Montserrat:wght@400;500;600;700&display=swap" rel="stylesheet">
<style>
  :root {
    --page-bg: #ece7df;
    --teal-deep: #08738c;
    --teal-mid: #1b97a3;
    --teal-soft: #38aaae;
    --teal-pale: #e4f4f9;
    --teal-text: #3ab0b3;
    --author-light: #8fd2d5;
    --white: #ffffff;
    --ink: #111111;
  }
  * { margin: 0; padding: 0; box-sizing: border-box; }
  html, body {
    width: 1200px; height: 900px; overflow: hidden;
    background: var(--page-bg);
  }
  .spread {
    position: absolute; left: 40px; top: 61px;
    width: 1120px; height: 778px;
    display: flex;
    box-shadow: 0 6px 18px rgba(0,0,0,0.18);
  }
  /* Back cover */
  .back-cover {
    width: 521px; height: 100%;
    background: linear-gradient(35deg, var(--teal-soft) 0%, var(--teal-mid) 45%, var(--teal-deep) 100%);
    color: var(--white);
    position: relative;
  }
  .back-author {
    position: absolute; left: 75px; top: 100px;
    font-family: 'Montserrat', sans-serif; font-weight: 500; font-size: 17px;
  }
  .back-title {
    position: absolute; left: 76px; top: 122px;
    font-family: 'Bebas Neue', sans-serif; font-size: 37px; line-height: 1; font-weight: 400;
  }
  .back-blurb {
    position: absolute; left: 78px; top: 186px; width: 344px;
    font-family: 'Montserrat', sans-serif; font-weight: 500;
    font-size: 11.2px; line-height: 14.2px; text-align: justify;
  }
  .back-blurb p + p { margin-top: 14.2px; }
  /* Spine */
  .spine {
    width: 78px; height: 100%;
    background: var(--white);
    border-right: 1px solid #333;
    position: relative;
    overflow: hidden;
  }
  .spine-author, .spine-title {
    position: absolute; writing-mode: vertical-rl; white-space: nowrap;
  }
  .spine-author {
    left: 24px; top: 40px;
    font-family: 'Montserrat', sans-serif; font-weight: 500; font-size: 28px;
    color: var(--ink); line-height: 1;
  }
  .spine-title {
    left: 17px; top: 340px;
    font-family: 'Bebas Neue', sans-serif; font-size: 50px; line-height: 1;
    color: var(--teal-text);
  }
  /* Front cover */
  .front-cover {
    width: 521px; height: 100%;
    background: var(--white);
    position: relative; overflow: hidden;
  }
  .endorsement {
    position: absolute; top: 24px; left: 0; width: 100%;
    text-align: center;
    font-family: 'Montserrat', sans-serif; font-size: 13.5px; color: var(--ink);
    line-height: 17px;
  }
  .endorsement cite { display: block; font-style: normal; font-weight: 700; font-size: 13px; }
  .cover-illustration {
    position: absolute; left: 2px; top: 80px; width: 498px; height: 698px;
    border-radius: 240px 240px 0 0;
    background: linear-gradient(215deg, var(--teal-pale) 0%, #9fd3d8 22%, var(--teal-soft) 45%, var(--teal-mid) 70%, var(--teal-deep) 100%);
  }
  .front-title {
    position: absolute; left: 0; top: 174px; width: 500px;
    text-align: center;
    font-family: 'Bebas Neue', sans-serif; font-size: 86px; line-height: 0.84; font-weight: 400;
    color: var(--white);
  }
  .front-author {
    position: absolute; left: 0; top: 712px; width: 500px;
    text-align: center;
    font-family: 'Montserrat', sans-serif; font-weight: 600; font-size: 27px;
    letter-spacing: 0.3em; color: var(--author-light);
  }
</style>
</head>
<body>
  <main class="spread">
    <section class="back-cover">
      <p class="back-author">Elias Marrow, MD</p>
      <h2 class="back-title">TALES OF QUIET HARBORS</h2>
      <div class="back-blurb">
        <p>Lorem ipsum dolor sit amet, consectetur adipiscing elit. Suspendisse nec lobortis ligula. Proin sit amet orci at massa accumsan tincidunt eget et massa. Fusce varius ultrices mattis. Aliquam erat volutpat. Curabitur finibus mauris erat, at ornare nulla commodo non. Vestibulum nisi magna, volutpat vel neque id, feugiat varius dolor. Donec faucibus congue dolor. Duis fringilla posuere aliquet. Morbi iaculis eleifend mauris ut aliquam. Vestibulum ante ipsum primis in faucibus orci luctus et ultrices posuere cubilia curae; Fusce ut tincidunt eros. Aliquam tincidunt, turpis in finibus elementum, ipsum diam volutpat neque, vel tristique nulla ipsum eget nisl. Suspendisse lobortis turpis a finibus auctor. Curabitur ut lectus et arcu vestibulum dapibus. Class aptent taciti sociosqu ad litora torquent per conubia nostra, per inceptos himenaeos. Ut ut magna sed mi vulputate pharetra.</p>
        <p>Phasellus lorem nisi, consectetur vitae lacinia sit amet, cursus ut elit. Mauris at posuere sem. Sed felis tellus, egestas eu congue sed, rhoncus eget mauris. Vestibulum posuere ipsum turpis, et hendrerit tortor vehicula quis. Nunc pharetra, velit vitae venenatis scelerisque, libero quam scelerisque diam, sit amet commodo velit elit in diam. Vestibulum ante ipsum primis in faucibus orci luctus et ultrices posuere cubilia curae; Cras efficitur dictum orci, ut semper purus facilisis id. Sed bibendum venenatis tortor. In aliquam odio a enim elementum, at venenatis lorem tincidunt. Nulla consequat eros vel quam faucibus, vitae dictum mi euismod. Vivamus interdum massa euismod augue fringilla, at fermentum felis cursus.</p>
      </div>
    </section>

    <section class="spine">
      <span class="spine-author">Elias Marrow, MD</span>
      <span class="spine-title">TALES OF QUIET HARBORS</span>
    </section>

    <section class="front-cover">
      <blockquote class="endorsement">
        “An incredible guide to protecting your mind and memories.”
        <cite>-Dr Nadia Brennan, MD</cite>
      </blockquote>
      <div class="cover-illustration" role="img" aria-label="Teal gradient profile silhouette of a human head with a dashed outline around the brain area"></div>
      <h1 class="front-title">TALES OF<br>QUIET HARBORS</h1>
      <p class="front-author">Elias Marrow, MD</p>
    </section>
  </main>
</body>
</html>
```